依頼詳細
ページに使用したいキャッチフレーズ:
個性的な道を究め、劇的に生きる人生を選択する
それがMoonhollow

参考にしたいURL:
https://www.kenmori-ux.brelo.jp/
https://www.sorimachikeigo.com/member-lounge

ムーンホロウクラブのHP:
https://www.ruvo.co.jp/moonhollow/

ページに使用したいテキスト:
『Moonhollow Clubとは

「あなたの好きなことは何ですか?」
好きなことを徹底追求し、“好き”を個性に。
そして、個性を武器にしながら“才能”へと伸ばしていくことで、
人生の構想力が磨かれ、あなたの人生は切り拓かれていきます。

誰かに敷かれたレールに乗りたいのか?
型にはまらない人生を創造したいのか?
一度きりの人生を、自分はどう生きたいか?

「自分らしい」人生を実現しよう!。』

採択後、デザインに利用した、デザインデータもお送りください。
(特に、画像ファイルは必ず送ってください)

何かご不明な点がございましたら、お気軽にお申し付けください。

※ 過去の制作実績をそのままご提案いただいたり、他社のポートフォリオをそのまま掲載することは恐れ入りますが、ご遠慮いただけますと幸いです。
サイトURL
http://moonhollowclub.jp
ページ数
1ページ
希望イメージ
シンプル 複雑
単色 カラフル
暗い 明るい
日常 高級
遊び心 厳粛
未来的 伝統的
女性的 男性的
希望する色
赤系、黄・オレンジ系、ジェンダーニュートラルなデザイン
納品ファイル
• イラストレーター形式 (.ai)
• PNG形式 (.png)
補足説明
デザインに利用した、デザインデータ(画像など)もお送り頂きますようお願い致します。

素晴らしいデザインをありがとうございました。

素晴らしいデザインをありがとうございました。

```html
<!DOCTYPE html>
<html lang="ja">
<head>
<meta charset="utf-8">
<title>Moonhollow Club</title>
<link href="https://fonts.googleapis.com/css2?family=Noto+Serif+JP:wght@400;500;700&family=Playfair+Display:ital,wght@0,400;1,400&display=swap" rel="stylesheet">
<style>
:root{
  --red:#e0283c;
  --red-dark:#c51f31;
  --ink:#2a2a2a;
  --muted:#777;
  --paper:#ffffff;
  --footer:#ececec;
}
*{box-sizing:border-box;margin:0;padding:0}
html,body{width:1200px;height:2988px;overflow:hidden;background:var(--paper)}
body{position:relative;font-family:"Noto Serif JP",serif;color:var(--ink)}
.abs{position:absolute}

/* header */
.site-header{position:absolute;left:0;top:0;width:1200px;height:80px;z-index:5}
.brand{position:absolute;left:70px;top:26px;font-size:26px;font-weight:500;color:var(--ink);letter-spacing:.02em}
.global-nav{position:absolute;left:800px;top:70px;display:flex;gap:26px;font-size:12px;color:var(--ink)}
.header-actions{position:absolute;left:860px;top:22px;display:flex;gap:12px}
.btn-red{display:inline-block;background:var(--red);color:#fff;font-size:12px;padding:7px 18px;letter-spacing:.05em}

/* hero */
.hero{position:absolute;left:0;top:0;width:1200px;height:1180px;
  background:linear-gradient(180deg,#f4f4f3 0%,#ebe8e4 30%,#cfc7be 55%,#ddd7d0 75%,#f5f4f2 100%)}
.catch{position:absolute;left:0;top:270px;width:1200px;text-align:center;font-size:24px;line-height:2.6;letter-spacing:.28em;color:#3a3230}
.catch .sub{font-size:20px;letter-spacing:.35em}

.about{position:absolute;left:312px;top:600px;width:576px;height:520px;background:#fff;
  border:1px solid #d9a8ae;outline:1px solid #f0d7da;outline-offset:-8px;text-align:center;padding-top:42px}
.about h2{font-size:22px;font-weight:500;letter-spacing:.1em;display:inline-block;padding:0 20px 10px;border-bottom:1px solid var(--red)}
.about p{font-size:13px;line-height:2.2;margin-top:22px;letter-spacing:.04em}
.about .closing{margin-top:18px}
.photo-globe{position:absolute;left:220px;top:990px;width:150px;height:210px;
  background:linear-gradient(180deg,#d9d2cb,#a43a3e 55%,#6d3d3a);z-index:2}
.photo-landmark{position:absolute;left:760px;top:1010px;width:140px;height:180px;
  background:linear-gradient(180deg,#e6e9ec,#b8bcc0 60%,#7e8388);z-index:2}

/* movies */
.movies{position:absolute;left:0;top:1200px;width:1200px;height:420px;background:var(--red)}
.movies-title{position:absolute;left:40px;top:26px;font-family:"Playfair Display",serif;font-size:62px;line-height:.95;color:#fff;font-weight:400}
.movies-label{position:absolute;left:0;width:1200px;top:60px;text-align:center;color:#fff;font-size:26px;letter-spacing:.15em}
.movies-more{position:absolute;left:820px;top:64px;border:1px solid #fff;color:#fff;font-size:12px;padding:6px 20px}
.video-row{position:absolute;left:40px;top:190px;display:flex;gap:22px}
.video-card{width:262px;height:200px;background:linear-gradient(135deg,#b7c4d8,#7b4f6a 55%,#e8d2c6);position:relative}
.video-card::after{content:"";position:absolute;left:50%;top:50%;width:46px;height:32px;margin:-16px 0 0 -23px;background:rgba(255,255,255,.85);border-radius:8px}
.arrow{position:absolute;width:40px;height:40px}

/* blog */
.blog{position:absolute;left:0;top:1690px;width:1200px}
.blog-title{text-align:center;font-size:34px;font-weight:500;letter-spacing:.2em}
.blog-sub{text-align:center;font-size:12px;color:var(--red);letter-spacing:.2em;margin-top:2px}
.blog-arrows{position:absolute;left:1030px;top:60px;display:flex;gap:20px}
.city{position:absolute;left:0;top:2000px;width:1200px;height:600px;
  background:linear-gradient(180deg,#cfe0ef 0%,#9fb7cc 40%,#5b6f84 70%,#3c4650 100%)}
.blog-row{position:absolute;left:20px;top:1800px;display:flex;gap:12px;z-index:2}
.blog-card{width:222px;background:#fff;box-shadow:0 2px 8px rgba(0,0,0,.15)}
.blog-photo{height:120px;background:linear-gradient(135deg,#e8c9b5,#8c6c5c 60%,#c7b6a9)}
.blog-body{padding:10px 12px 14px;text-align:center}
.blog-date{font-size:11px;color:var(--red)}
.blog-text{font-size:13px;line-height:1.6;margin-top:4px}

/* board */
.board{position:absolute;left:312px;top:2240px;width:576px;height:420px;background:#fff;text-align:center;padding-top:40px;z-index:3}
.board h2{font-size:34px;font-weight:500;letter-spacing:.2em;margin-top:8px}
.board .en{font-size:12px;color:var(--red);letter-spacing:.15em}
.board .note{font-size:12px;margin-top:42px}
.search{margin:26px auto 0;width:440px;height:40px;border:1px solid #bbb;position:relative}

/* footer */
.site-footer{position:absolute;left:0;top:2720px;width:1200px;height:268px;background:var(--footer)}
.footer-brand{position:absolute;left:110px;top:50px;font-size:26px;font-weight:500}
.footer-tag{position:absolute;left:110px;top:104px;font-size:13px;letter-spacing:.15em}
.footer-actions{position:absolute;left:860px;top:50px;display:flex;gap:12px}
.footer-links{position:absolute;left:960px;top:100px;list-style:none;font-size:11px;line-height:1.8}
.copyright{position:absolute;left:110px;top:234px;font-size:10px;color:var(--muted)}
</style>
</head>
<body>

<div class="hero" role="img" aria-label="霧の中に続く線路と、留学する学生たちの写真"></div>

<header class="site-header">
  <div class="brand">Moonhollow Club</div>
  <div class="header-actions"><span class="btn-red">無料会員登録</span><span class="btn-red">ログイン</span></div>
  <nav class="global-nav"><span>お問い合わせ</span><span>活動内容</span><span>海外留学情報</span><span>お知らせ</span></nav>
</header>

<div class="catch">
  個性的な道を究め、<br>劇的に生きる人生を選択する<br><span class="sub">それがMoonhollow</span>
</div>

<section class="about">
  <h2>Moonhollow Clubとは</h2>
  <p>「あなたの好きなことは何ですか?」<br>好きなことを徹底追求し、“好き”を個性に。<br>そして、個性を武器にしながら“才能”へと伸ばしていくことで、<br>人生の構想力が磨かれ、あなたの人生は切り拓かれていきます。</p>
  <p>誰かに敷かれたレールに乗りたいのか?<br>型にはまらない人生を創造したいのか?<br>一度きりの人生を、自分はどう生きたいか?</p>
  <p class="closing">「自分らしい」人生を実現しよう!</p>
</section>
<div class="photo-globe" role="img" aria-label="地球儀を持つ女性の写真"></div>
<div class="photo-landmark" role="img" aria-label="海外の名所の写真"></div>

<section class="movies">
  <div class="movies-title">New.<br>Movies</div>
  <div class="movies-label">新着動画</div>
  <div class="movies-more">一覧を見る</div>
  <div class="video-row">
    <div class="video-card" role="img" aria-label="動画サムネイル"></div>
    <div class="video-card" role="img" aria-label="動画サムネイル"></div>
    <div class="video-card" role="img" aria-label="動画サムネイル"></div>
    <div class="video-card" role="img" aria-label="動画サムネイル"></div>
  </div>
  <svg class="arrow" style="left:4px;top:270px" viewBox="0 0 40 40"><path d="M24 10 L14 20 L24 30" fill="none" stroke="#fff" stroke-width="3"/></svg>
  <svg class="arrow" style="left:1156px;top:270px" viewBox="0 0 40 40"><path d="M16 10 L26 20 L16 30" fill="none" stroke="#fff" stroke-width="3"/></svg>
</section>

<div class="city" role="img" aria-label="橋と高層ビルが並ぶ都市の写真"></div>

<section class="blog">
  <div class="blog-title">ブログ</div>
  <div class="blog-sub">Blog</div>
  <div class="blog-arrows">
    <svg width="20" height="24" viewBox="0 0 20 24"><path d="M14 4 L6 12 L14 20" fill="none" stroke="#555" stroke-width="2"/></svg>
    <svg width="20" height="24" viewBox="0 0 20 24"><path d="M6 4 L14 12 L6 20" fill="none" stroke="#555" stroke-width="2"/></svg>
  </div>
</section>
<div class="blog-row">
  <article class="blog-card"><div class="blog-photo" role="img" aria-label="ブログ記事の写真"></div><div class="blog-body"><div class="blog-date">2020.3.3</div><div class="blog-text">今できる!<br>家でできる留学準備</div></div></article>
  <article class="blog-card"><div class="blog-photo" role="img" aria-label="ブログ記事の写真"></div><div class="blog-body"><div class="blog-date">2020.3.2</div><div class="blog-text">コロナ禍の海外留学<br>オンライン講座の案内</div></div></article>
  <article class="blog-card"><div class="blog-photo" role="img" aria-label="ブログ記事の写真"></div><div class="blog-body"><div class="blog-date">2020.3.1</div><div class="blog-text">今できる!<br>家でできる留学準備</div></div></article>
  <article class="blog-card"><div class="blog-photo" role="img" aria-label="ブログ記事の写真"></div><div class="blog-body"><div class="blog-date">2020.2.28</div><div class="blog-text">コロナ禍の海外留学<br>オンライン講座の案内</div></div></article>
  <article class="blog-card"><div class="blog-photo" role="img" aria-label="ブログ記事の写真"></div><div class="blog-body"><div class="blog-date">2020.2.27</div><div class="blog-text">今できる!<br>家でできる留学準備</div></div></article>
</div>

<section class="board">
  <svg width="40" height="34" viewBox="0 0 40 34"><path d="M4 3 H36 V23 H18 L10 31 V23 H4 Z" fill="none" stroke="var(--red)" stroke-width="2.5"/><circle cx="13" cy="13" r="2" fill="var(--red)"/><circle cx="20" cy="13" r="2" fill="var(--red)"/><circle cx="27" cy="13" r="2" fill="var(--red)"/></svg>
  <h2>掲示板</h2>
  <div class="en">Notice board</div>
  <p class="note">チャットルームを利用する場合は、ログインしてください。</p>
  <div class="search">
    <svg class="abs" style="right:12px;top:10px" width="20" height="20" viewBox="0 0 20 20"><circle cx="8" cy="8" r="6" fill="none" stroke="#666" stroke-width="2"/><path d="M12.5 12.5 L18 18" stroke="#666" stroke-width="2"/></svg>
  </div>
</section>

<footer class="site-footer">
  <div class="footer-brand">Moonhollow Club</div>
  <div class="footer-tag">個性的な道を究め、劇的に生きる</div>
  <div class="footer-actions"><span class="btn-red">無料会員登録</span><span class="btn-red">ログイン</span></div>
  <ul class="footer-links"><li>ホーム</li><li>活動内容</li><li>海外留学情報</li><li>お知らせ</li><li>お問い合わせ</li><li>ブログ</li></ul>
  <div class="copyright">©2020 Moonhollow Club All Rights Reserved.</div>
</footer>

</body>
</html>
```